BUSINESS CARD DESIGN FOR BRELWICK INSTITUTE

Hi, Obviously using the brelwick institute design done by you.

Details :-
BRELLWICK INSTITUTE
Registration No. 48270915K
274 Quarry Lane #07-14
Harbourview Plaza Singapore 264813
TEL +65 6481 2730
dorn@brelwickinstitutte.com.sg
www.brelwickinstitute.com.sg

Back Surface:

Halvorn QBTE Approved Centre
Brelwick Practical Accounting Training (BPAT)
Corporate Tax Preparation Workshop
GST Practical Workshop
Management Accounting Training
Business Skills Training Programs
PMET Self Improvement Workshops

Pls note later to add in 2 or 3 logos of partners

Project Deadline Extended Reason: Obviously 2 days is too short to produce a good one. Added Wednesday, May 11, 2016

Dear All,The green color for the main logo should be a darker in shade. Not the one I posted.Also black color is out. Except the name and designation of employee should be preferably in black.All note there should space for logos of business partners (about 3 to 4).Thanks! Added Monday, May 16, 2016

Would be uploading various partners logos for inclusion. Added Monday, July 4, 2016

Age 18 to 35

Business

See above project description

9bcb3c
f78f20
faa54b
fbc994
abd036
cadf82

• Simple and professional on the front.
• Not excessively colorful

```html
<!DOCTYPE html>
<html lang="en">
<head>
<meta charset="utf-8">
<title>Brelwick Institute Business Card</title>
<link rel="stylesheet" href="https://fonts.googleapis.com/css2?family=Open+Sans:wght@400;600;700&display=swap">
<style>
  :root {
    --bg: #e9e7e4;
    --orange: #ea9419;
    --white: #ffffff;
    --green: #3f7d1f;
    --ink: #111111;
    --muted: #4a4a4a;
    --badge-red: #c8322c;
    --badge-blue: #2b5ea8;
    --badge-green: #5aa832;
    --badge-grey: #bdbdbd;
    --badge-dark: #1a1a1a;
  }
  * { margin: 0; padding: 0; box-sizing: border-box; }
  html, body { width: 1200px; height: 900px; overflow: hidden; }
  body {
    background: var(--bg);
    font-family: "Open Sans", Arial, sans-serif;
    color: var(--ink);
    position: relative;
  }
  .card {
    position: absolute;
    background: var(--orange);
    box-shadow: 0 6px 18px rgba(0,0,0,0.18);
    overflow: hidden;
  }
  /* Front */
  .card-front { left: 78px; top: 34px; width: 588px; height: 364px; }
  .front-header {
    height: 149px; background: var(--white);
    display: flex; align-items: center; gap: 12px;
    padding: 0 0 0 32px;
  }
  .brand-mark {
    width: 22px; height: 22px; border-radius: 50%;
    background: var(--green); flex: none;
  }
  .brand-name {
    color: var(--green); font-weight: 700;
    font-size: 34px; line-height: 40px;
  }
  .front-body { position: relative; padding: 12px 0 0 31px; }
  .company { font-size: 15px; font-weight: 700; line-height: 20px; }
  .registration { font-size: 15px; font-weight: 600; line-height: 22px; }
  .registration span { font-weight: 400; }
  .person-name { font-size: 20px; font-weight: 700; margin-top: 8px; line-height: 26px; }
  .person-title { font-size: 15.5px; line-height: 22px; }
  .contact-list { list-style: none; margin-top: 6px; }
  .contact-list li {
    display: flex; align-items: center; gap: 8px;
    font-size: 15.5px; line-height: 21.5px; color: var(--ink);
  }
  .contact-list svg { width: 12px; height: 12px; flex: none; }
  .address {
    position: absolute; right: 36px; top: 120px;
    text-align: right; font-size: 15.5px; line-height: 25px; font-style: normal;
  }
  /* Back */
  .card-back { left: 388px; top: 506px; width: 567px; height: 351px; }
  .service-list { list-style: none; padding: 23px 0 0 30px; }
  .service-list li {
    font-size: 15.5px; line-height: 30px; position: relative; padding-left: 15px;
  }
  .service-list li::before {
    content: ""; position: absolute; left: 0; top: 12px;
    width: 7px; height: 7px; border-radius: 50%; background: var(--ink);
  }
  .partners-tab {
    position: absolute; left: 385px; top: 212px; width: 149px; height: 32px;
    background: var(--white); color: var(--muted);
    font-size: 13px; text-align: center; line-height: 38px;
  }
  .partners-strip {
    position: absolute; left: 0; bottom: 0; width: 100%; height: 107px;
    background: var(--white);
    display: flex; align-items: center; justify-content: space-between;
    padding: 0 33px 0 19px;
  }
  .partner-badge { display: block; }
</style>
</head>
<body>

<section class="card card-front">
  <header class="front-header">
    <span class="brand-mark" aria-hidden="true"></span>
    <div class="brand-name">Brelwick Institute</div>
  </header>
  <div class="front-body">
    <p class="company">BRELLWICK INSTITUTE</p>
    <p class="registration">Registration No. <span>48270915K</span></p>
    <p class="person-name">Marcus Hale</p>
    <p class="person-title">Managing Director</p>
    <ul class="contact-list">
      <li>
        <svg viewBox="0 0 12 12" aria-hidden="true"><path d="M2.5 0.8l2 2.3-1 1.3c.7 1.5 1.8 2.6 3.3 3.3l1.3-1 2.3 2-1 2c-4.6-.3-8-3.7-8.3-8.3z" fill="#111"/></svg>
        +65 6481 2730
      </li>
      <li>
        <svg viewBox="0 0 12 12" aria-hidden="true"><rect x="3" y="0.5" width="6" height="11" rx="1" fill="none" stroke="#111" stroke-width="1.3"/><circle cx="6" cy="9.6" r="0.7" fill="#111"/></svg>
        +65 6481 2730
      </li>
      <li>
        <svg viewBox="0 0 12 12" aria-hidden="true"><rect x="0.5" y="2.5" width="11" height="7" fill="#111"/><path d="M0.5 2.5l5.5 4 5.5-4" fill="none" stroke="#ea9419" stroke-width="1"/></svg>
        dorn@brelwickinstitutte.com.sg
      </li>
      <li>
        <svg viewBox="0 0 12 12" aria-hidden="true"><circle cx="6" cy="6" r="5.5" fill="#111"/><path d="M3 4.5h2l1 2-1 2M7 2.5l1.5 1.5-.5 2 1.5 1" fill="none" stroke="#ea9419" stroke-width="0.9"/></svg>
        www.brelwickinstitute.com.sg
      </li>
    </ul>
    <address class="address">
      274 Quarry Lane<br>
      #07-14 Harbourview Plaza<br>
      Singapore 264813
    </address>
  </div>
</section>

<section class="card card-back">
  <ul class="service-list">
    <li>Halvorn QBTE Approved Centre</li>
    <li>Brelwick Work-Based Practical Accounting Training</li>
    <li>Corporate Tax Preparation Workshop</li>
    <li>GST Practical Workshop</li>
    <li>Management Accounting Training</li>
    <li>Business Skills Training Programs</li>
    <li>PMET Self Improvement Workshops</li>
  </ul>
  <div class="partners-tab">OUR PARTNERS</div>
  <div class="partners-strip">
    <svg class="partner-badge" width="100" height="36" role="img" aria-label="Partner badge"><rect width="100" height="36" fill="var(--badge-red)" opacity="0.85"/></svg>
    <svg class="partner-badge" width="42" height="42" role="img" aria-label="Partner badge"><circle cx="21" cy="21" r="20" fill="var(--badge-blue)"/></svg>
    <svg class="partner-badge" width="70" height="36" role="img" aria-label="Partner badge"><ellipse cx="35" cy="18" rx="34" ry="17" fill="var(--badge-red)"/></svg>
    <svg class="partner-badge" width="46" height="46" role="img" aria-label="Certificate badge"><rect width="46" height="46" rx="3" fill="var(--badge-green)"/></svg>
    <svg class="partner-badge" width="46" height="46" role="img" aria-label="Certificate badge"><rect width="46" height="46" rx="3" fill="var(--badge-green)"/></svg>
    <svg class="partner-badge" width="88" height="12" role="img" aria-label="Partner badge"><rect width="88" height="12" fill="var(--badge-grey)"/></svg>
    <svg class="partner-badge" width="62" height="50" role="img" aria-label="Partner badge"><rect width="62" height="50" rx="2" fill="var(--badge-dark)"/></svg>
  </div>
</section>

</body>
</html>
```